Harbrook Techlink Solutions

We need a Logo and Website for our company based in London. We are a IT recruitment company . We provide quality resources to top IT company across UK.

Industry/Entity Type

It Company

Number of Pages Required

4 page

```html
<!DOCTYPE html>
<html lang="en">
<head>
<meta charset="utf-8">
<title>Harbrook Techlink Solutions</title>
<link rel="stylesheet" href="https://fonts.googleapis.com/css2?family=Open+Sans:wght@400;600;700&display=swap">
<style>
:root{
  --gold:#c8913a;
  --gold-dark:#a9752a;
  --gold-light:#d9a551;
  --navy:#15243a;
  --navy-panel:#1d3148;
  --footer:#132132;
  --footer-base:#0c1726;
  --ink:#2a2a2a;
  --muted:#777;
  --line:#e2e2e2;
  --band:#e7e9ec;
  --white:#fff;
}
*{box-sizing:border-box;margin:0;padding:0}
html,body{width:1200px;height:2338px;overflow:hidden}
body{font-family:"Open Sans",Arial,sans-serif;color:var(--ink);background:var(--white);position:relative}
.abs{position:absolute}

/* header */
.site-header{position:absolute;left:0;top:0;width:1200px;height:117px;border-top:3px solid var(--gold);background:var(--white)}
.brand{position:absolute;left:112px;top:33px;display:flex;align-items:center;gap:12px}
.brand-dot{width:46px;height:46px;border-radius:50%;background:var(--navy)}
.brand-name{font-size:21px;line-height:24px;font-weight:400;color:var(--navy);text-transform:uppercase}
.main-nav{position:absolute;left:425px;top:54px;display:flex;gap:0}
.main-nav a{font-size:12px;color:#333;text-decoration:none;text-transform:uppercase;margin-right:40px}
.main-nav a.active{color:var(--gold)}
.btn-signin{position:absolute;left:961px;top:33px;width:127px;height:50px;background:linear-gradient(var(--gold-light),var(--gold-dark));color:#fff;font-size:12px;text-transform:uppercase;display:flex;align-items:center;justify-content:center;border-radius:2px}

/* hero */
.hero{position:absolute;left:0;top:117px;width:1200px;height:547px}
.hero-photo{position:absolute;inset:0;background:linear-gradient(100deg,#8a6e5a 0%,#c9c3bc 30%,#e8e6e2 55%,#b9b7b3 75%,#dcdad6 100%)}
.hero-box{position:absolute;left:268px;top:243px;width:662px;height:221px;background:rgba(70,70,70,.55);text-align:center;color:#fff}
.hero-box h1{font-size:25px;font-weight:600;margin-top:25px;text-transform:uppercase}
.hero-box p{font-size:11px;line-height:26px;width:560px;margin:10px auto 0}
.hero-cta{display:inline-flex;margin-top:18px;height:57px}
.hero-cta span{width:172px;background:linear-gradient(var(--gold-light),var(--gold-dark));display:flex;align-items:center;justify-content:center;font-size:18px;text-transform:uppercase}
.hero-cta i{width:55px;background:#f2f2f2;display:flex;align-items:center;justify-content:center}
.hero-slider{position:absolute;left:505px;top:508px;width:190px;height:4px;background:rgba(255,255,255,.35)}
.hero-slider b{position:absolute;left:65px;top:0;width:60px;height:4px;background:var(--gold)}

/* search */
.search-band{position:absolute;left:0;top:664px;width:1200px;height:111px;background:var(--gold)}
.field{position:absolute;top:28px;height:57px;border:1px solid rgba(255,255,255,.85);color:#fff;font-size:11px;padding:0 19px;display:flex;align-items:center}
.btn-find{position:absolute;left:868px;top:28px;width:172px;height:57px;background:linear-gradient(#fff,#d9d9d9);color:var(--gold);font-size:17px;display:flex;align-items:center;justify-content:center;gap:6px;text-transform:uppercase;border-radius:2px}

/* section titles */
.section-title{position:absolute;left:0;width:1200px;text-align:center;font-size:25px;font-weight:600;color:var(--ink);text-transform:uppercase}

/* profiles */
.profile{position:absolute;top:860px;width:225px;height:307px;background:#efefef;overflow:hidden}
.profile-photo{position:absolute;left:45px;top:18px;width:135px;height:165px;background:linear-gradient(#d9dadc,#bfc2c6)}
.profile svg{position:absolute;left:0;top:0}
.profile-name{position:absolute;left:0;top:213px;width:225px;text-align:center;font-size:13px;color:#fff;font-weight:600}
.profile-name em{font-style:normal;font-weight:400;color:#9aa4b0}
.btn-bio{position:absolute;left:58px;top:247px;width:110px;height:37px;border:1px solid var(--gold);color:var(--gold);font-size:13px;display:flex;align-items:center;justify-content:center;text-transform:uppercase}

/* stats + about */
.stats{position:absolute;left:0;top:1225px;width:420px;height:358px;background:linear-gradient(135deg,#f4f5f6,#e3e6ea 60%,#eef0f2)}
.stat{position:absolute;left:112px;display:flex;align-items:center}
.stat-icon{width:72px;height:72px;border-radius:50%;background:var(--gold);display:flex;align-items:center;justify-content:center}
.stat-text{margin-left:10px}
.stat-text b{display:block;font-size:31px;font-weight:400;line-height:32px;color:#222}
.stat-text span{font-size:14px;color:#444}
.about{position:absolute;left:420px;top:1225px;width:780px;height:358px;background:var(--navy-panel);color:#fff}
.about h2{position:absolute;left:53px;top:43px;font-size:25px;font-weight:600;text-transform:uppercase}
.about p{position:absolute;left:53px;top:92px;width:668px;font-size:11px;line-height:26px}
.btn-contact{position:absolute;left:53px;top:250px;width:190px;height:57px;background:linear-gradient(var(--gold-light),var(--gold-dark));font-size:15px;display:flex;align-items:center;justify-content:center;text-transform:uppercase;font-weight:600}

/* feedback */
.quote{position:absolute;top:1686px;width:320px}
.quote-avatar{position:absolute;left:0;top:4px;width:72px;height:72px;border-radius:50%;border:3px solid #eee;background:linear-gradient(#d5d8dc,#aeb3b9)}
.quote p{margin-left:83px;font-size:11.5px;line-height:26px;color:#777;text-align:justify}
.quote cite{display:block;margin-left:83px;font-style:normal;font-size:15px;color:#333;margin-top:2px}
.dots{position:absolute;left:576px;top:1830px;display:flex;gap:5px}
.dots i{width:13px;height:13px;border-radius:50%;background:#ccc}
.dots i.on{background:var(--gold)}

/* partners */
.partners{position:absolute;left:0;top:1884px;width:1200px;height:182px;background:var(--band)}
.partner{position:absolute;top:62px;width:56px;height:56px;background:#9a9a9a}

/* footer */
.site-footer{position:absolute;left:0;top:2066px;width:1200px;height:192px;background:var(--footer);color:#fff}
.site-footer h3{position:absolute;top:38px;font-size:16px;font-weight:600;text-transform:uppercase}
.contact-line{position:absolute;left:112px;font-size:11px;line-height:24px;display:flex;gap:10px}
.map{position:absolute;left:343px;top:79px;width:300px;height:94px;background:linear-gradient(120deg,#cfd9e3,#b7c8d8 50%,#d9e1e8);border:2px solid #5f6e80}
.newsletter-text{position:absolute;left:732px;top:68px;width:360px;font-size:11px;line-height:20px}
.email{position:absolute;left:732px;top:114px;width:230px;height:38px;background:#25364b;font-size:10px;display:flex;align-items:center;padding-left:17px}
.btn-submit{position:absolute;left:976px;top:114px;width:112px;height:38px;background:linear-gradient(var(--gold-light),var(--gold-dark));font-size:12px;display:flex;align-items:center;justify-content:center;text-transform:uppercase}
.footer-base{position:absolute;left:0;top:2258px;width:1200px;height:80px;background:var(--footer-base);color:#9aa4b0;font-size:11px}
.footer-base p{position:absolute;left:112px;top:32px}
.social{position:absolute;left:987px;top:29px;display:flex;gap:4px}
.social i{width:19px;height:19px;background:#4a5a6e}
</style>
</head>
<body>

<header class="site-header">
  <div class="brand"><span class="brand-dot"></span><span class="brand-name">Harbrook Techlink<br>Solutions</span></div>
  <nav class="main-nav">
    <a class="active" href="#">Home</a><a href="#">Jobs</a><a href="#">Candidates</a><a href="#">About</a><a href="#">Blog</a><a href="#">Contact us</a>
  </nav>
  <div class="btn-signin">Sign in</div>
</header>

<section class="hero">
  <div class="hero-photo" role="img" aria-label="Photo of a smiling team of four young professionals giving thumbs up"></div>
  <div class="hero-box">
    <h1>Harbrook Techlink Solutions</h1>
    <p>Lorem ipsum dolor sit amet, consectetur adipiscing elit. Nulla ullamcorper porttitor tristique. Pellentesque venenatis at orci non cursus. Sed a semper metus.</p>
    <div class="hero-cta"><span>Sign up now</span><i><svg width="14" height="14" viewBox="0 0 14 14"><path d="M1 7h10M7 2l5 5-5 5" stroke="#c8913a" stroke-width="2.4" fill="none"/></svg></i></div>
  </div>
  <div class="hero-slider"><b></b></div>
</section>

<section class="search-band">
  <div class="field" style="left:160px;width:334px">Keywords</div>
  <div class="field" style="left:513px;width:333px">Location</div>
  <div class="btn-find"><svg width="15" height="15" viewBox="0 0 15 15"><circle cx="6" cy="6" r="4.5" stroke="#c8913a" stroke-width="2" fill="none"/><path d="M9.5 9.5l4 4" stroke="#c8913a" stroke-width="2.4"/></svg>Find now</div>
</section>

<h2 class="section-title" style="top:803px">Latest profiles</h2>

<div class="profile" style="left:112px">
  <div class="profile-photo" role="img" aria-label="Portrait of a candidate in a dark suit"></div>
  <svg width="225" height="307"><polygon points="0,192 225,179 225,307 0,307" fill="#15243a"/></svg>
  <div class="profile-name">Tom Ashby <em>/ Designer</em></div><div class="btn-bio">Full bio</div>
</div>
<div class="profile" style="left:362px">
  <div class="profile-photo" role="img" aria-label="Portrait of a candidate in a dark suit"></div>
  <svg width="225" height="307"><polygon points="0,192 225,179 225,307 0,307" fill="#15243a"/></svg>
  <div class="profile-name">Ray Dalton <em>/ Designer</em></div><div class="btn-bio">Full bio</div>
</div>
<div class="profile" style="left:612px">
  <div class="profile-photo" role="img" aria-label="Portrait of a candidate in a dark suit"></div>
  <svg width="225" height="307"><polygon points="0,192 225,179 225,307 0,307" fill="#15243a"/></svg>
  <div class="profile-name">Tom Ashby <em>/ Designer</em></div><div class="btn-bio">Full bio</div>
</div>
<div class="profile" style="left:862px">
  <div class="profile-photo" role="img" aria-label="Portrait of a candidate in a dark suit"></div>
  <svg width="225" height="307"><polygon points="0,192 225,179 225,307 0,307" fill="#15243a"/></svg>
  <div class="profile-name">Ray Dalton <em>/ Designer</em></div><div class="btn-bio">Full bio</div>
</div>

<section class="stats" role="img" aria-label="Faded photo of an office meeting">
  <div class="stat" style="top:27px"><div class="stat-icon"><svg width="30" height="24" viewBox="0 0 30 24"><circle cx="15" cy="7" r="5" fill="#fff"/><circle cx="6" cy="9" r="3.5" fill="#fff"/><circle cx="24" cy="9" r="3.5" fill="#fff"/><path d="M7 23c0-6 4-9 8-9s8 3 8 9z M0 22c0-4 3-7 6-7 1 0 2 0 3 1-2 2-3 4-3 6z M30 22c0-4-3-7-6-7-1 0-2 0-3 1 2 2 3 4 3 6z" fill="#fff"/></svg></div><div class="stat-text"><b>1450</b><span>Candidates</span></div></div>
  <div class="stat" style="top:130px"><div class="stat-icon"><svg width="22" height="28" viewBox="0 0 22 28"><path d="M2 2h12l6 6v18H2z" fill="none" stroke="#fff" stroke-width="2.2"/><path d="M6 13h10M6 17h10M6 21h10" stroke="#fff" stroke-width="2"/></svg></div><div class="stat-text"><b>124</b><span>Companies</span></div></div>
  <div class="stat" style="top:233px"><div class="stat-icon"><svg width="26" height="26" viewBox="0 0 26 26"><rect x="2" y="11" width="5" height="13" fill="#fff"/><path d="M9 11l5-9c2 0 3 1 3 3l-1 5h7c1.5 0 2.5 1 2 2.5l-2.5 9.5c-.4 1.3-1.3 2-2.5 2H9z" fill="#fff"/></svg></div><div class="stat-text"><b>871</b><span>Success Stories</span></div></div>
</section>

<section class="about">
  <h2>Who we are</h2>
  <p>Lorem ipsum dolor sit amet, consectetur adipiscing elit. Nulla purus nisl, tincidunt in tellus id, pellentesque ullamcorper risus. Phasellus commodo, elit vel facilisis viverra, diam orci eleifend tellus, id semper libero ipsum sed augue. Proin a fermentum justo. Cras dictum vel quam convallis varius. Praesent cursus enim non nunc interdum auctor. Phasellus id mi nibh. Donec at lorem lobortis, vehicula dui in, luctus eros. Suspendisse pretium pulvinar ullamcorper. Donec sit amet felis eros. Donec pretium finibus mi, vel dictum est cursus et. Vivamus aliquam efficitur libero sed vehicula</p>
  <div class="btn-contact">Contact us now !</div>
</section>

<h2 class="section-title" style="top:1624px">Feedback about us</h2>

<div class="quote" style="left:112px">
  <div class="quote-avatar" role="img" aria-label="Portrait of a client"></div>
  <p>Lorem ipsum dolor sit amet, consectetur adipiscing elit. Nulla purus nisl, tincidunt in tellus id, pellentesque ullamcorper risus. Phasellus commodo.</p>
  <cite>- Ray Dalton</cite>
</div>
<div class="quote" style="left:445px">
  <div class="quote-avatar" role="img" aria-label="Portrait of a client"></div>
  <p>Praesent cursus enim non nunc interdum auctor. Phasellus id mi nibh. Donec at lorem lobortis, vehicula dui in, luctus eros. Suspendisse pretium.</p>
  <cite>- Ray Dalton</cite>
</div>
<div class="quote" style="left:779px">
  <div class="quote-avatar" role="img" aria-label="Portrait of a client"></div>
  <p>Aenean in consequat tortor, mattis aliquam nunc. Donec vel accumsan orci, aliquet bibendum elit. Fusce tellus tellus, gravida quis sagittis at, ornare egestas felis.</p>
  <cite>- Ray Dalton</cite>
</div>
<div class="dots"><i></i><i class="on"></i><i></i></div>

<section class="partners">
  <div class="partner" style="left:152px;border-radius:50%"></div>
  <div class="partner" style="left:323px"></div>
  <div class="partner" style="left:495px;border-radius:50%"></div>
  <div class="partner" style="left:666px"></div>
  <div class="partner" style="left:838px;border-radius:50%"></div>
  <div class="partner" style="left:1008px"></div>
</section>

<footer class="site-footer">
  <h3 style="left:112px">Quick contact</h3>
  <div class="contact-line" style="top:72px"><svg width="8" height="12" viewBox="0 0 8 12"><path d="M4 12C1 7 0 5.5 0 4a4 4 0 018 0c0 1.5-1 3-4 8z" fill="#c8913a"/></svg><span>12 Quay Lane<br>London, E15 2PX</span></div>
  <div class="contact-line" style="top:131px"><svg width="12" height="12" viewBox="0 0 12 12"><path d="M2 0l3 3-1.5 1.5c.8 1.8 2.2 3.2 4 4L9 7l3 3-2 2C5 12 0 7 0 2z" fill="#c8913a"/></svg><span>020 7946 0183</span></div>
  <h3 style="left:340px">Our location</h3>
  <div class="map" role="img" aria-label="Street map of the office location"></div>
  <h3 style="left:732px">Newsletter signup</h3>
  <p class="newsletter-text">Lorem ipsum dolor sit amet, consectetuer adipiscing elit, sed diam nonummy nibh</p>
  <div class="email">Email Address</div>
  <div class="btn-submit">Submit</div>
</footer>
<div class="footer-base">
  <p>Copyright@2016 Harbrook Techlink Solutions. All Right Reserved.</p>
  <div class="social"><i></i><i></i><i></i><i></i></div>
</div>

</body>
</html>
```